Cool modern, tech Business card design

Looking for a new business card design for our Managed IT Services company. We would like 2 sides, with the logo one one side horizontally and then the information on the back in either vertical or horizontal. We want our colors from the logo incorporated but also would like to see the color gray in there as well.

Target Market(s)

IT, Information Technology, Tech, Service

Industry/Entity Type

It Service

Contact Information for Business Card

Carl Penner
Managing Partner
(P)555-271-4830 ext xxx
(F)555-271-4831
www.brixtelcore.com

Font styles to use
Sans Serif

Colors
959595
000000
ec1f27

Requirements
Must have
• Logo on one side with some nice design or pattern
• Information on back in either vertical or horizontal format
Nice to have
• For it to look cool, tech, modern, stand out.

```html
<!DOCTYPE html>
<html lang="en">
<head>
<meta charset="utf-8">
<title>Brixtelcore Business Card</title>
<link href="https://fonts.googleapis.com/css2?family=Fira+Sans:wght@400;500&display=swap" rel="stylesheet">
<style>
  :root {
    --brand-red: #ec1f27;
    --brand-grey: #959595;
    --card-black: #000000;
    --page-white: #ffffff;
    --text-white: #ffffff;
    --shape-grey: rgba(149, 149, 149, 0.16);
    --shape-red: rgba(120, 10, 14, 0.55);
  }
  html, body {
    margin: 0;
    width: 1200px;
    height: 1200px;
    overflow: hidden;
    background: var(--page-white);
    font-family: "Fira Sans", sans-serif;
  }
  .card {
    position: absolute;
    left: 249px;
    width: 702px;
    height: 402px;
    background: var(--card-black);
    overflow: hidden;
  }
  .card--front { top: 157px; }
  .card--back { top: 663px; }
  .card__stripe {
    position: absolute;
    left: 0; top: 0; bottom: 0;
    width: 29px;
    background: var(--brand-red);
  }
  .card__accent-square {
    position: absolute;
    left: 646px; top: 19px;
    width: 46px; height: 46px;
    border-radius: 10px;
    background: var(--shape-red);
    transform: rotate(45deg);
  }
  .card__backdrop-shape {
    position: absolute;
    left: 560px; top: 92px;
    width: 170px; height: 300px;
    border-radius: 36px;
    background: var(--shape-grey);
  }
  .wordmark {
    position: absolute;
    display: flex;
    align-items: center;
    gap: 12px;
    color: var(--brand-grey);
    font-weight: 400;
    white-space: nowrap;
  }
  .wordmark__square {
    background: var(--brand-red);
    border-radius: 3px;
  }
  .card--front .wordmark {
    left: 0; right: 0;
    top: 180px;
    justify-content: center;
    font-size: 56px;
  }
  .card--front .wordmark__square { width: 26px; height: 26px; }
  .card--back .wordmark {
    left: 60px; width: 260px;
    top: 212px;
    justify-content: center;
    font-size: 40px;
  }
  .card--back .wordmark__square { width: 18px; height: 18px; }
  .card__divider {
    position: absolute;
    left: 349px; top: 102px;
    width: 2px; height: 197px;
    background: var(--brand-red);
  }
  .contact {
    position: absolute;
    right: 85px; top: 124px;
    text-align: right;
    color: var(--text-white);
  }
  .contact__name {
    margin: 0;
    font-size: 31px;
    font-weight: 500;
    line-height: 38px;
  }
  .contact__title {
    margin: 0 0 12px;
    font-size: 19px;
    color: var(--brand-red);
    line-height: 26px;
  }
  .contact__line {
    margin: 0;
    font-size: 18px;
    font-weight: 500;
    line-height: 29px;
  }
  .contact__label { color: var(--brand-red); font-weight: 400; }
  .contact__web {
    margin: 2px 0 0;
    font-size: 18px;
    color: var(--brand-red);
    line-height: 26px;
  }
</style>
</head>
<body>
  <section class="card card--front">
    <div class="card__stripe"></div>
    <div class="card__accent-square"></div>
    <div class="card__backdrop-shape"></div>
    <div class="wordmark"><span class="wordmark__square"></span>brixtelcore</div>
  </section>

  <section class="card card--back">
    <div class="card__stripe"></div>
    <div class="card__accent-square"></div>
    <div class="card__backdrop-shape"></div>
    <div class="wordmark"><span class="wordmark__square"></span>brixtelcore</div>
    <div class="card__divider"></div>
    <div class="contact">
      <p class="contact__name">Carl Penner</p>
      <p class="contact__title">Managing Partner</p>
      <p class="contact__line"><span class="contact__label">(P)</span> 555-271-4830</p>
      <p class="contact__line"><span class="contact__label">(F)</span> 555-271-4831</p>
      <p class="contact__web">www.brixtelcore.com</p>
    </div>
  </section>
</body>
</html>
```